Business Cards for new orthopaedic surgery practice

My husband and I are starting our own orthopaedic surgery practice. We are looking for a business card that is uniform, but one will have my name/title and the other will have his. You can just create one design with my name on it for now. But when I choose your design as the winning design I will ask that you add another copy with his name/title.

We are looking for classy, simple, elite all in one. We like dark blues/a little gold/yellow. Something that goes with our logo. We want our logo incorporated. Here is all the info you need:
Business name: RV Spine & Vitality Center
Location: 38915 North Bramble Ave
Willowmere, FL 33480
Phone: 954-218-4630
Fax: 954-571-2846
Email: info@myrvspine.example

Names: Lucinda Ferrow, M.D.
Board Certified Hand and Upper Extremity Surgeon

Emeka Dlunga, M.D.
Board Certified Hip & Knee Replacement/General Orthopaedic Surgeon

Can decide what you want to put on the back. Maybe a slogan:
Built on Trust. Guided by Care

I am just going to upload our logo. The only thing is if we select you as the winning design, the location, and phone numbers may change. We will need your help to update that once fully solidified.

Industry/Entity Type

Medical

Contact Information for Business Card

Colors
0054AA
0677BA
7BADD7
CADEEF
E8F1F8
0094D4
00A9DD
6FCCEA
C7EBF8
E9F6FB

Requirements
Must have
• class, appeal,
Should not have
• We want to air on the side of masculine if we are looking at masculine vs. feminine feel. But we still want it classy, sophisticated, and something we will love

```html
<!DOCTYPE html>
<html lang="en">
<head>
<meta charset="utf-8">
<title>RV Spine &amp; Vitality Center – Business Card</title>
<link rel="stylesheet" href="https://fonts.googleapis.com/css2?family=Montserrat:wght@400;500;600;700&display=swap">
<style>
  :root {
    --backdrop: #3a3a3c;
    --navy: #1f3580;
    --navy-deep: #17296a;
    --navy-light: #3a55a6;
    --ink: #1d2433;
    --cyan: #1aaee0;
    --logo-blue: #1f3a8f;
    --paper: #ffffff;
  }
  * { box-sizing: border-box; margin: 0; padding: 0; }
  html, body {
    width: 1200px; height: 689px; overflow: hidden;
    background: var(--backdrop);
    font-family: "Montserrat", sans-serif;
  }
  .canvas {
    position: relative; width: 1200px; height: 689px;
    display: flex; align-items: center; justify-content: center; gap: 40px;
  }
  .card {
    position: relative; width: 540px; height: 309px;
    border-radius: 22px; overflow: hidden;
    box-shadow: 0 14px 34px rgba(0,0,0,.45);
  }

  /* Front */
  .card--front {
    background: linear-gradient(120deg, var(--navy-light) 0%, var(--navy) 45%, var(--navy-deep) 100%);
    color: #fff;
  }
  .front-brand {
    position: absolute; left: 0; right: 0; top: 86px;
    display: flex; align-items: center; justify-content: center; gap: 14px;
  }
  .brand-dot {
    width: 22px; height: 22px; border-radius: 50%;
    background: var(--navy-deep); flex: none;
  }
  .front-brand .brand-name {
    font-weight: 700; font-size: 27px; letter-spacing: .5px;
    color: var(--navy-deep); text-transform: uppercase; line-height: 1.15;
  }
  .tagline {
    position: absolute; left: 0; right: 0; bottom: 46px;
    text-align: center; font-size: 15px; font-weight: 500; letter-spacing: 1px;
  }

  /* Back */
  .card--back {
    background: var(--paper); color: var(--ink);
    padding: 24px 26px;
    display: flex; flex-direction: column; justify-content: center;
  }
  .back-brand {
    display: flex; align-items: center; justify-content: center; gap: 10px;
    margin-bottom: 16px;
  }
  .back-brand .brand-dot { width: 18px; height: 18px; background: var(--logo-blue); }
  .back-brand .brand-name {
    font-weight: 700; font-size: 17px; color: var(--logo-blue);
    text-transform: uppercase; letter-spacing: .4px;
  }
  .doctor { text-align: center; margin-bottom: 9px; }
  .doctor-name { color: var(--cyan); font-weight: 700; font-size: 25px; line-height: 1.15; }
  .doctor-title { font-size: 11.5px; font-weight: 500; white-space: nowrap; }
  .back-footer {
    display: flex; justify-content: center; align-items: stretch; gap: 18px;
    margin-top: 12px;
  }
  .address { font-size: 12px; line-height: 1.55; text-align: right; font-style: normal; }
  .address .practice { color: var(--cyan); font-weight: 500; }
  .divider { width: 1.5px; background: var(--cyan); }
  .contact-list { list-style: none; font-size: 12px; line-height: 1.55; }
  .contact-list li { display: flex; align-items: center; gap: 7px; }
  .contact-list svg { width: 11px; height: 11px; fill: var(--cyan); flex: none; }
</style>
</head>
<body>
<main class="canvas">
  <section class="card card--front" aria-label="Card front">
    <div class="front-brand">
      <span class="brand-dot"></span>
      <span class="brand-name">RV Spine &amp;<br>Vitality Center</span>
    </div>
    <p class="tagline">Built on Trust. Guided by Care</p>
  </section>

  <section class="card card--back" aria-label="Card back">
    <div class="back-brand">
      <span class="brand-dot"></span>
      <span class="brand-name">RV Spine &amp; Vitality Center</span>
    </div>
    <div class="doctor">
      <h2 class="doctor-name">Lucinda Ferrow, M.D.</h2>
      <p class="doctor-title">Board Certified Hand and Upper Extremity Surgeon</p>
    </div>
    <div class="doctor">
      <h2 class="doctor-name">Emeka Dlunga, M.D.</h2>
      <p class="doctor-title">Board Certified Hip &amp; Knee Replacement/General Orthopaedic Surgeon</p>
    </div>
    <div class="back-footer">
      <address class="address">
        <span class="practice">RV Orthopaedic Partners</span><br>
        38915 North Bramble Ave<br>
        Willowmere, FL 33480
      </address>
      <span class="divider"></span>
      <ul class="contact-list">
        <li><svg viewBox="0 0 24 24"><path d="M6.6 10.8a15 15 0 0 0 6.6 6.6l2.2-2.2c.3-.3.7-.4 1-.2 1.1.4 2.3.6 3.6.6.6 0 1 .4 1 1V20c0 .6-.4 1-1 1A17 17 0 0 1 3 4c0-.6.4-1 1-1h3.5c.6 0 1 .4 1 1 0 1.3.2 2.5.6 3.6.1.3 0 .7-.2 1z"/></svg>954-218-4630</li>
        <li><svg viewBox="0 0 24 24"><path d="M6 2h12v5H6zM4 8h16a2 2 0 0 1 2 2v7h-4v5H6v-5H2v-7a2 2 0 0 1 2-2zm4 8v4h8v-4z"/></svg>954-571-2846</li>
        <li><svg viewBox="0 0 24 24"><path d="M2 5h20v14H2zm2 2v.5l8 5 8-5V7z"/></svg>info@myrvspine.example</li>
      </ul>
    </div>
  </section>
</main>
</body>
</html>
```